Global Weight loss program

we need a business card based in Brooklyn , NY called ZestwellPRO . Mara Tullin Opdegard the founder and creator of ZestwellPRO Movement. A business based around nutrition, health, Whole Foods and fitness.

Industry/Entity Type

Food Service

Contact Information for Business Card

Phone number : 718-402-3859
website www.zestwellpro.example
email : mara@zestwellpro.example

Font styles to use
Sans Serif

Requirements
Must have
• logo colors
• green black and gold
Nice to have
• must be simple and sharp.
Should not have
• pictures of items

```html
<!DOCTYPE html>
<html lang="en">
<head>
<meta charset="utf-8">
<title>ZestwellPRO Business Card</title>
<link href="https://fonts.googleapis.com/css2?family=Open+Sans:wght@400;600&family=Roboto:wght@400;500&display=swap" rel="stylesheet">
<style>
  :root {
    --page-bg: #e6e6e6;
    --card-dark: #2f2f2f;
    --card-light: #ffffff;
    --ink-dark: #2b2b2b;
    --ink-light: #ffffff;
    --muted: #8a8a8a;
    --green: #6cc02c;
    --green-deep: #3f9a1e;
  }
  * { margin: 0; padding: 0; box-sizing: border-box; }
  html, body { width: 1200px; height: 880px; overflow: hidden; }
  body {
    background: var(--page-bg);
    font-family: "Open Sans", sans-serif;
    position: relative;
  }
  .card {
    position: absolute;
    top: 292px;
    width: 520px;
    height: 297px;
    border-radius: 18px;
    box-shadow: 0 10px 30px rgba(0,0,0,0.18);
    overflow: hidden;
  }
  .card--back { left: 50px; background: var(--card-dark); }
  .card--front { left: 630px; background: var(--card-light); }

  .brand { display: flex; flex-direction: column; align-items: center; }
  .brand__row { display: flex; align-items: center; gap: 10px; }
  .brand__dot {
    width: 22px; height: 22px; border-radius: 50%;
    background: var(--green);
  }
  .brand__name {
    font-weight: 600;
    font-size: 34px;
    letter-spacing: -0.5px;
    line-height: 1;
  }
  .brand__tagline {
    margin-top: 6px;
    font-size: 10px;
    letter-spacing: 2px;
    color: var(--muted);
  }

  .card--back .brand {
    position: absolute; left: 0; right: 0; top: 100px;
  }
  .card--back .brand__name { color: var(--ink-light); }
  .card--back .website {
    position: absolute; left: 0; right: 0; top: 200px;
    text-align: center;
    color: var(--ink-light);
    font-size: 14px;
    letter-spacing: 4px;
  }

  .card--front .brand {
    position: absolute; left: 20px; width: 220px; top: 118px;
  }
  .card--front .brand__name { color: var(--ink-dark); font-size: 30px; }
  .divider {
    position: absolute; left: 262px; top: 78px;
    width: 1px; height: 140px;
    background: var(--green);
  }
  .person { position: absolute; left: 292px; top: 82px; }
  .person__name {
    font-family: "Roboto", sans-serif;
    font-weight: 500; font-size: 19px;
    color: var(--green);
  }
  .person__role {
    font-family: "Roboto", sans-serif;
    font-size: 15px; color: var(--ink-dark);
  }
  .contacts {
    position: absolute; left: 292px; top: 150px;
    list-style: none;
    font-family: "Roboto", sans-serif;
    font-size: 14px; color: var(--ink-dark);
  }
  .contacts li { display: flex; align-items: center; gap: 8px; height: 22px; }
  .contacts svg { width: 16px; height: 16px; flex: none; }
</style>
</head>
<body>
  <section class="card card--back">
    <div class="brand">
      <div class="brand__row">
        <span class="brand__dot"></span>
        <span class="brand__name">ZestwellPRO</span>
      </div>
      <span class="brand__tagline">Fitness, Nutrition and Health</span>
    </div>
    <p class="website">www.zestwellpro.example</p>
  </section>

  <section class="card card--front">
    <div class="brand">
      <div class="brand__row">
        <span class="brand__dot"></span>
        <span class="brand__name">ZestwellPRO</span>
      </div>
      <span class="brand__tagline">Fitness, Nutrition and Health</span>
    </div>

    <span class="divider"></span>

    <div class="person">
      <p class="person__name">Mara Opdegard</p>
      <p class="person__role">Founder</p>
    </div>

    <ul class="contacts">
      <li>
        <svg viewBox="0 0 16 16" aria-hidden="true"><circle cx="8" cy="8" r="7.2" fill="none" stroke="var(--green)" stroke-width="1.2"/><rect x="5.6" y="3.8" width="4.8" height="8.4" rx="0.8" fill="none" stroke="var(--green)" stroke-width="1"/><circle cx="8" cy="10.8" r="0.5" fill="var(--green)"/></svg>
        718-402-3859
      </li>
      <li>
        <svg viewBox="0 0 16 16" aria-hidden="true"><circle cx="8" cy="8" r="7.2" fill="var(--green)"/><rect x="4.2" y="5.3" width="7.6" height="5.4" fill="#fff"/><path d="M4.2 5.3 L8 8.4 L11.8 5.3" fill="none" stroke="var(--green)" stroke-width="0.9"/></svg>
        mara@zestwellpro.example
      </li>
      <li>
        <svg viewBox="0 0 16 16" aria-hidden="true"><circle cx="8" cy="8" r="7.2" fill="var(--green)"/><circle cx="8" cy="8" r="4" fill="none" stroke="#fff" stroke-width="0.9"/><ellipse cx="8" cy="8" rx="1.8" ry="4" fill="none" stroke="#fff" stroke-width="0.8"/><path d="M4 8 H12" stroke="#fff" stroke-width="0.8"/></svg>
        www.zestwellpro.example
      </li>
    </ul>
  </section>
</body>
</html>
```